Stationary and Business Cards
Bright Harbor Legal
Project: Stationary and Business Cards
Stationary and Business Cards - Law
Creative Brief
Professional
Marek Vandellin
Director Of Operations
412 Willowmere Cres Toronto, Ontario M4R 7J9
Marek@brightharborlegal-example.ca
brightharborlegal-example.ca
Serving the Greater Toronto Area region.
Our goal is to provide our customers with outstanding service through dedication and excellence and to ensure we are the industry leader. Our charges will be fair, competitive and driven by our level of effort expanded.

```html
<!DOCTYPE html>
<html lang="en">
<head>
<meta charset="utf-8">
<title>Bright Harbor Legal – Stationery and Business Cards</title>
<link href="https://fonts.googleapis.com/css2?family=Arimo:wght@400;700&display=swap" rel="stylesheet">
<style>
  :root{
    --ink:#0f0f0f;
    --paper:#ffffff;
    --stage:#e4e2df;
    --accent:#c8321f;
    --gold:#e29a34;
    --silver-1:#f4f4f4;
    --silver-2:#bdbdbd;
    --text-dark:#222;
    --text-light:#f2f2f2;
  }
  *{box-sizing:border-box;margin:0;padding:0}
  html,body{width:1200px;height:896px;overflow:hidden}
  body{background:var(--stage);font-family:'Arimo',Arial,sans-serif;position:relative;color:var(--text-dark)}

  .sheet{position:absolute;background:var(--paper);box-shadow:0 2px 8px rgba(0,0,0,.18);overflow:hidden}

  /* brand lockup */
  .brand{display:flex;align-items:center;gap:8px}
  .brand-dot{border-radius:50%;background:var(--accent);flex:none;border:2px solid var(--gold)}
  .brand-name{font-weight:700;color:var(--text-light);text-transform:uppercase;letter-spacing:.02em;white-space:nowrap}

  .accent-rule{height:3px;background:linear-gradient(90deg,var(--accent),var(--gold))}

  /* letterhead */
  .letterhead{left:40px;top:86px;width:560px;height:724px}
  .letterhead .head{position:absolute;left:24px;right:24px;top:26px;height:44px;background:var(--ink);padding:0 12px;display:flex;align-items:center}
  .letterhead .head .brand-dot{width:26px;height:26px}
  .letterhead .head .brand-name{font-size:15px}
  .letterhead .head-rule{position:absolute;left:24px;right:24px;top:70px}
  .letterhead .foot{position:absolute;left:0;right:0;bottom:0;height:50px;background:var(--ink);color:var(--text-light);font-size:8.5px;line-height:1.5;text-align:center;padding-top:13px}

  /* business cards */
  .card{width:252px;height:144px;top:130px;background:var(--ink);border-radius:8px}
  .card-front{left:640px}
  .card-back{left:908px;display:flex;align-items:center;justify-content:center}
  .card-front .brand{position:absolute;left:12px;top:10px}
  .card-front .brand-dot{width:18px;height:18px}
  .card-front .brand-name{font-size:10px}
  .card-front .info{position:absolute;left:0;right:0;top:40px;height:70px;background:linear-gradient(180deg,var(--silver-1),var(--silver-2));border-top:2px solid var(--accent);display:flex;justify-content:space-between;padding:8px 12px;font-size:6.5px;line-height:1.45}
  .card-front .person{text-align:right;align-self:center}
  .card-front .person-name{font-size:10px;font-weight:700}
  .card-front .person-title{font-size:7px}
  .card-front .strip{position:absolute;left:0;right:0;bottom:12px;font-size:6px;color:var(--text-light);text-align:center}
  .card-back .brand{flex-direction:column;gap:8px}
  .card-back .brand-dot{width:46px;height:46px}
  .card-back .brand-name{font-size:11px}

  /* envelopes */
  .envelope{left:640px;width:520px;height:226px}
  .envelope-back{top:294px;background:var(--paper)}
  .envelope-back svg{position:absolute;left:0;top:0}
  .envelope-back .brand{position:absolute;left:0;right:0;top:14px;flex-direction:column;gap:6px}
  .envelope-back .brand-dot{width:40px;height:40px}
  .envelope-back .brand-name{font-size:11px}

  .envelope-front{top:540px}
  .envelope-front .head{position:absolute;left:0;right:0;top:22px;height:40px;background:var(--ink);padding:0 14px;display:flex;align-items:center}
  .envelope-front .head .brand-dot{width:22px;height:22px}
  .envelope-front .head .brand-name{font-size:13px}
  .envelope-front .head-rule{position:absolute;left:0;right:0;top:62px}
  .envelope-front .return{position:absolute;left:14px;top:76px;font-size:8.5px;line-height:1.45}
  .envelope-front .foot{position:absolute;left:0;right:0;bottom:0;height:40px;background:var(--ink);color:var(--text-light);font-size:7.5px;line-height:1.55;text-align:right;padding:9px 14px 0}
</style>
</head>
<body>

<section class="sheet letterhead" aria-label="Letterhead">
  <header class="head">
    <div class="brand"><span class="brand-dot"></span><span class="brand-name">Bright Harbor Legal</span></div>
  </header>
  <div class="accent-rule head-rule"></div>
  <footer class="foot">
    412 Willowmere Cres Toronto, Ontario M4R 7J9 &nbsp;Phone: 416-555-0148 &nbsp;Cell: 416-555-0172<br>
    Fax: 416-555-0193 &nbsp;Email: Marek@brightharborlegal-example.ca &nbsp;www.brightharborlegal-example.ca
  </footer>
</section>

<section class="sheet card card-front" aria-label="Business card front">
  <div class="brand"><span class="brand-dot"></span><span class="brand-name">Bright Harbor Legal</span></div>
  <div class="info">
    <div class="contact">
      412 Willowmere Cres<br>Toronto, Ontario M4R 7J9<br>Phone: 416-555-0148<br>Cell: 416-555-0172<br>Fax: 416-555-0193
    </div>
    <div class="person">
      <div class="person-name">Marek Vandellin</div>
      <div class="person-title">Director Of Operations</div>
    </div>
  </div>
  <div class="strip">Serving the Greater Toronto Area</div>
</section>

<section class="sheet card card-back" aria-label="Business card back">
  <div class="brand"><span class="brand-dot"></span><span class="brand-name">Bright Harbor Legal</span></div>
</section>

<section class="sheet envelope envelope-back" aria-label="Envelope back">
  <svg width="520" height="226" viewBox="0 0 520 226" aria-hidden="true">
    <path d="M0 0 H520 V20 L290 100 Q260 110 230 100 L0 20 Z" fill="#0f0f0f"/>
    <path d="M0 20 L230 100 Q260 110 290 100 L520 20" fill="none" stroke="#c8321f" stroke-width="2"/>
  </svg>
  <div class="brand"><span class="brand-dot"></span></div>
</section>

<section class="sheet envelope envelope-front" aria-label="Envelope front">
  <header class="head">
    <div class="brand"><span class="brand-dot"></span><span class="brand-name">Bright Harbor Legal</span></div>
  </header>
  <div class="accent-rule head-rule"></div>
  <address class="return" style="font-style:normal">412 Willowmere Cres<br>Toronto, Ontario<br>M4R 7J9</address>
  <footer class="foot">
    Phone: 416-555-0148 &nbsp;Cell: 416-555-0172<br>
    Fax: 416-555-0193 &nbsp;Email: Marek@brightharborlegal-example.ca &nbsp;www.brightharborlegal-example.ca
  </footer>
</section>

</body>
</html>
```